"Bright Hollow Craft Dwellings" need a busines Card Design got Builder

We need a business card design for a company based in Milford, Michigancalled Bright Hollow Craft Dwellings - has been recognized as a premier custom home builder. Distinguished by outstanding craftmanship and timeless beauty. Our custom home can be found in the most prestigious communities in Michigan. The homes are built with ICF (insulated concrete homes) which is green, allergy free, fire free, mold free and quitter. Our slogan "building one dream at a Time" and also we are ICF distributor for the state of Michigan

Target Market(s)

Anyone who is making over $100,000 a year and who wants to have totally custom built home. Ages from 29 up to 60 years old

Industry/Entity Type

Concrete

Contact Information for Business Card

we want to use - green, black, gray or blue colors - we want to look different with our business cards, because we built homes only with ICF, green, healthier and highly energy efficient homes.

Requirements
Must have
• I have logo that I attached and we have been using the logo (the only green home)
Nice to have
• should look quality business card,

```html
<!DOCTYPE html>
<html lang="en">
<head>
<meta charset="utf-8">
<title>Bright Hollow Craft Dwellings — Business Card</title>
<link rel="stylesheet" href="https://fonts.googleapis.com/css2?family=Open+Sans:wght@400;600;700&display=swap">
<style>
  :root {
    --page: #e8e5e1;
    --card: #1c1c1c;
    --card-edge: #2a2a2a;
    --sweep-dark: #0b0b0b;
    --sweep-light: #3a3a3a;
    --mark-front: #2f2f2f;
    --name-front: #262626;
    --green: #8cc63f;
    --white: #ffffff;
    --divider: #7cb82f;
  }
  html, body {
    margin: 0;
    width: 1200px;
    height: 1000px;
    overflow: hidden;
    background: var(--page);
    font-family: "Open Sans", Arial, sans-serif;
  }
  .card {
    position: absolute;
    left: 250px;
    width: 695px;
    height: 413px;
    border-radius: 24px;
    background: var(--card);
    overflow: hidden;
    box-shadow: 0 2px 6px rgba(0,0,0,.25);
  }
  .card--front { top: 65px; }
  .card--back { top: 523px; }
  .card__sweeps { position: absolute; inset: 0; }
  .brand {
    position: absolute;
    display: flex;
    align-items: center;
  }
  .brand__dot { border-radius: 50%; flex: none; }
  .brand__name {
    text-transform: uppercase;
    font-weight: 400;
    line-height: 0.95;
    letter-spacing: 0.5px;
  }
  .card--front .brand { left: 80px; top: 130px; }
  .card--front .brand__dot { width: 150px; height: 150px; background: var(--mark-front); margin-right: 22px; }
  .card--front .brand__name { font-size: 31px; color: var(--name-front); }
  .card--back .brand { left: 110px; top: 50px; }
  .card--back .brand__dot { width: 136px; height: 136px; background: var(--green); margin-right: 18px; }
  .card--back .brand__name { font-size: 26px; color: var(--white); }
  .slogan {
    position: absolute;
    left: 0; right: 0; top: 210px;
    text-align: center;
    color: var(--white);
    font-weight: 700;
    font-size: 17px;
    margin: 0;
  }
  .person {
    position: absolute;
    right: 357px; top: 256px;
    text-align: right;
    color: var(--white);
    font-size: 17px;
    line-height: 22px;
  }
  .person__name { font-weight: 700; margin: 0 0 17px; }
  .person__address { margin: 0; }
  .divider {
    position: absolute;
    left: 354px; top: 258px;
    width: 2px; height: 84px;
    background: var(--divider);
  }
  .contact {
    position: absolute;
    left: 370px; top: 256px;
    margin: 0; padding: 0;
    list-style: none;
    color: var(--white);
    font-size: 17px;
    line-height: 21px;
  }
  .contact li { display: flex; align-items: center; }
  .contact svg { width: 14px; height: 14px; margin-right: 8px; fill: var(--white); }
</style>
</head>
<body>

<section class="card card--front">
  <svg class="card__sweeps" viewBox="0 0 695 413" aria-hidden="true">
    <defs>
      <linearGradient id="sweepFront" x1="0" y1="0" x2="1" y2="1">
        <stop offset="0" stop-color="var(--sweep-light)"/>
        <stop offset="1" stop-color="var(--sweep-dark)"/>
      </linearGradient>
    </defs>
    <path d="M0,95 Q8,330 215,413 L0,413 Z" fill="url(#sweepFront)"/>
    <path d="M12,150 Q40,340 200,410" fill="none" stroke="#4a4a4a" stroke-width="1.5"/>
    <path d="M410,0 Q640,15 695,150 L695,0 Z" fill="url(#sweepFront)"/>
    <path d="M470,8 Q640,30 688,130" fill="none" stroke="#4a4a4a" stroke-width="1.5"/>
  </svg>
  <div class="brand">
    <span class="brand__dot"></span>
    <span class="brand__name">Bright Hollow<br>Craft Dwellings</span>
  </div>
</section>

<section class="card card--back">
  <svg class="card__sweeps" viewBox="0 0 695 413" aria-hidden="true">
    <defs>
      <linearGradient id="sweepBack" x1="0" y1="0" x2="1" y2="1">
        <stop offset="0" stop-color="var(--sweep-light)"/>
        <stop offset="1" stop-color="var(--sweep-dark)"/>
      </linearGradient>
    </defs>
    <path d="M0,120 Q10,340 230,413 L0,413 Z" fill="url(#sweepBack)"/>
    <path d="M14,170 Q45,350 215,410" fill="none" stroke="#4a4a4a" stroke-width="1.5"/>
    <path d="M430,0 Q650,15 695,140 L695,0 Z" fill="url(#sweepBack)"/>
    <path d="M490,8 Q645,30 688,120" fill="none" stroke="#4a4a4a" stroke-width="1.5"/>
  </svg>
  <div class="brand">
    <span class="brand__dot"></span>
    <span class="brand__name">Bright Hollow<br>Craft Dwellings</span>
  </div>
  <p class="slogan">"BUILDING ONE DREAM AT A TIME"</p>
  <div class="person">
    <p class="person__name">R. Martin Hale</p>
    <p class="person__address">218 Orchard Lane<br>Ste: 104 Maple Falls, Mi 48300</p>
  </div>
  <span class="divider"></span>
  <ul class="contact">
    <li><svg viewBox="0 0 16 16"><path d="M4 1l3 3-2 2c1 2 3 4 5 5l2-2 3 3-2 3C7 15 1 9 1 3z"/></svg>555-014-2730</li>
    <li><svg viewBox="0 0 16 16"><path d="M4 1h8v4H4zM1 6h14v6h-3v3H4v-3H1zM5 10v3h6v-3z"/></svg>555-014-2731</li>
    <li><svg viewBox="0 0 16 16"><path d="M1 3h14v10H1zM2 4l6 5 6-5z" fill-rule="evenodd"/></svg>mhale@brighthollow.com</li>
    <li><svg viewBox="0 0 16 16"><path d="M8 1a7 7 0 100 14A7 7 0 008 1zm0 1.5c.8 0 1.7 1.8 1.9 4.5H6.1C6.3 4.3 7.2 2.5 8 2.5zM2.6 7h2.3c0-1.6.3-3 .8-4A5.6 5.6 0 002.6 7zm0 2a5.6 5.6 0 003.1 4c-.5-1-.8-2.4-.8-4zm3.5 0h3.8c-.2 2.7-1.1 4.5-1.9 4.5S6.3 11.7 6.1 9zm5 0c0 1.6-.3 3-.8 4a5.6 5.6 0 003.1-4zm2.3-2a5.6 5.6 0 00-3.1-4c.5 1 .8 2.4.8 4z"/></svg>www.brighthollowdwellings.com</li>
  </ul>
</section>

</body>
</html>
```